Business Card Design Project : Tidewell Press

In preparation for market launch, Whistler's Tidewell Press require the development of a business card. Tidewell Press is a Community online publishing web portal. We provide the the city of Whistler located in B.C. (Canada) business directories, News, Classified ads, News, Events and blogs etc.

The main focus of the brand is to help local businesses to corporate with their online advertisement and marketing. Meeting our clients face to face is a must (B2B).

Target Market(s)

The target market is B2B customers. Business Owners to Marketing, advertising Managers

Industry/Entity Type

Business

Requirements
Must have
• - The business card will be two sided.
the BACK side will have our logo which consist of (icon, url,slogan) submited. The logo will be middle and centred.

The FRONT side should have company details:

Company Legal Name: FERNDALE TIDEWELL PRESS

Owen Marsk
Director of Sales & Marketing

www.ferndaletidewell.biz
owen@ferndaletidewell.biz

Phone: 555 014 3826
#2817 - 562 E. Harlow Ave.
Vancouver, B.C. K7P2R4 Canada
Nice to have
• - For the "FRONT" side of our business card. You can separate or re-arrange with our logo components (icon, logo,slogan). It does not have to be together.

Also our company legal name is rather long so arrange or organize the name in a way to make it shorter. Your experience and creativity will have to come in play.
Should not have
• should not have other colors beside logo color and black text (2 colors). Also nothing Three dimensional

```html
<!DOCTYPE html>
<html lang="en">
<head>
<meta charset="utf-8">
<title>Ferndale Tidewell Press – Business Card</title>
<link rel="stylesheet" href="https://fonts.googleapis.com/css2?family=Michroma&family=Open+Sans:wght@400;600&display=swap">
<style>
  :root {
    --brand-blue: #29a8e0;
    --brand-navy: #0f2a4a;
    --ink: #222222;
    --card-edge: #c9c9c9;
    --paper: #ffffff;
    --paper-shade: #e9e9e9;
  }
  * { box-sizing: border-box; margin: 0; padding: 0; }
  html, body {
    width: 1200px; height: 353px; overflow: hidden;
    background: var(--paper);
  }
  .sheet { position: relative; width: 1200px; height: 353px; }
  .card {
    position: absolute; top: 10px; width: 580px; height: 334px;
    border: 1px solid var(--card-edge);
    overflow: hidden;
  }
  /* Back side */
  .card--back {
    left: 10px;
    background: radial-gradient(ellipse at 50% 45%, var(--paper) 40%, var(--paper-shade) 100%);
    text-align: center;
  }
  .legal-name {
    position: absolute; top: 12px; left: 0; right: 0;
    font-family: "Michroma", sans-serif; font-weight: 400;
    font-size: 25px; letter-spacing: 1px; color: var(--brand-navy);
  }
  .brand-mark {
    position: absolute; top: 120px; left: 0; right: 0;
    display: flex; align-items: center; justify-content: center; gap: 16px;
    font-family: "Michroma", sans-serif; font-size: 38px; color: var(--brand-blue);
  }
  .brand-dot {
    width: 28px; height: 28px; border-radius: 50%; background: var(--brand-blue);
  }
  .slogan {
    position: absolute; bottom: 14px; left: 0; right: 0;
    font-family: "Michroma", sans-serif; font-size: 22px;
    letter-spacing: 4px; color: var(--brand-navy);
  }
  /* Front side */
  .card--front { left: 612px; background: var(--paper); }
  .front-band {
    position: absolute; top: 0; left: 0; right: 0; height: 138px;
    background: var(--brand-blue);
    display: flex; align-items: center; justify-content: center; gap: 14px;
    font-family: "Michroma", sans-serif; font-size: 32px; color: var(--paper);
  }
  .front-band .brand-dot { background: var(--paper); width: 24px; height: 24px; }
  .person-name {
    position: absolute; top: 150px; left: 0; right: 0; text-align: center;
    font-family: "Open Sans", sans-serif; font-size: 32px;
    letter-spacing: 4px; color: var(--ink);
  }
  .person-title {
    position: absolute; top: 202px; left: 0; right: 0; text-align: center;
    font-family: "Open Sans", sans-serif; font-size: 13px; color: var(--ink);
  }
  .contact {
    position: absolute; bottom: 12px;
    font-family: "Open Sans", sans-serif; font-size: 13.5px;
    line-height: 22px; color: var(--ink);
  }
  .contact--address { left: 16px; }
  .contact--online { right: 16px; text-align: left; }
  .contact--online p + p { margin-top: 20px; }
</style>
</head>
<body>
  <main class="sheet">
    <section class="card card--back" aria-label="Card back">
      <h1 class="legal-name">FERNDALE TIDEWELL PRESS</h1>
      <div class="brand-mark"><span class="brand-dot"></span>Tidewell Press</div>
      <p class="slogan">your information getaway</p>
    </section>

    <section class="card card--front" aria-label="Card front">
      <div class="front-band"><span class="brand-dot"></span>Tidewell Press</div>
      <h2 class="person-name">Owen Marsk</h2>
      <p class="person-title">Director of Sales &amp; Marketing</p>
      <address class="contact contact--address" style="font-style:normal">
        Phone: 555 014 3826<br>
        #2817 - 562 E. Harlow Ave.<br>
        Vancouver, B.C. K7P2R4 Canada
      </address>
      <div class="contact contact--online">
        <p>owen@ferndaletidewell.biz</p>
        <p>www.ferndaletidewell.biz</p>
      </div>
    </section>
  </main>
</body>
</html>
```